Need Catering Menu designed - design that we want is attached

Hi,
We need a new catering menu designed for our cafe.
I have attached our coffee menu, we would like it to follow the same kind of layout.
It needs to be A4, and can be double sided.
I have attached a word doc of our catering menu, so this is what needs to be on the catering menu you produce.
Also, our contact details need to be on both sides of the menu:
Visit us instore to discuss catering options, or call 0438 672 914 or email martha@velbrisco.com.au
I have also attached our new logo which I'd like incorporated into the menu
Doctors/Nurses
Hospital staff
University Students
Catering

```html
<!DOCTYPE html>
<html lang="en">
<head>
<meta charset="utf-8">
<title>Ward Rounds – Catering Menu</title>
<link rel="stylesheet" href="https://fonts.googleapis.com/css2?family=Cabin:ital,wght@0,400;0,500;0,600;1,400&display=swap">
<style>
:root{
  --paper:#ffffff;
  --board:#4e3f34;
  --board-light:#5c4b3e;
  --board-dark:#3f3229;
  --ink:#ffffff;
  --ink-soft:#efe9e3;
  --badge:#2e2430;
  --ribbon:#2b2330;
}
*{box-sizing:border-box;margin:0;padding:0}
html,body{width:800px;height:1200px;overflow:hidden;background:var(--paper)}
body{position:relative;font-family:"Cabin",sans-serif;color:var(--ink)}
.sheet{position:absolute;left:0;width:800px;
  background:radial-gradient(ellipse at 40% 35%,var(--board-light),var(--board) 55%,var(--board-dark))}
.sheet--front{top:30px;height:567px}
.sheet--back{top:607px;height:578px}
.brand{position:absolute;left:50%;transform:translateX(-50%);border-radius:50%;background:var(--badge);
  display:flex;align-items:center;justify-content:center;text-align:center;color:var(--ink-soft);
  font-weight:500;letter-spacing:2px;line-height:1.05}
.brand--large{top:12px;width:100px;height:100px;font-size:15px}
.brand--small{top:27px;width:60px;height:60px;font-size:9px;letter-spacing:1px}
.menu-title{position:absolute;left:0;width:100%;text-align:center;font-weight:400;letter-spacing:.5px}
.sheet--front .menu-title{top:127px;font-size:16px}
.sheet--back .menu-title{top:91px;font-size:12px}
.panel{position:absolute;border:2px solid var(--ink)}
.ribbon{position:absolute;display:flex;align-items:center;justify-content:center;text-align:center;
  color:var(--ink);line-height:1.15;letter-spacing:.5px}
.ribbon svg{position:absolute;inset:0;width:100%;height:100%;overflow:visible}
.ribbon span{position:relative}
.price-list{position:absolute;list-style:none;font-size:11px;font-weight:500}
.price-list li{display:flex;justify-content:space-between;height:17px;align-items:center}
.notes{position:absolute;font-size:8.5px;font-style:italic;line-height:17px}
.contact{position:absolute;font-style:italic}
.lunch{position:absolute;left:42px;top:165px;width:318px;font-size:8.8px;line-height:11.3px}
.lunch p{margin:0}
.lunch b{font-weight:600;font-style:normal}
.lunch i{font-style:italic;color:var(--ink-soft)}
.lunch .gap{height:11.3px}
</style>
</head>
<body>

<section class="sheet sheet--front">
  <div class="brand brand--large">WARD<br>ROUNDS</div>
  <h1 class="menu-title">CATERING MENU</h1>

  <div class="panel" style="left:32px;top:175px;width:338px;height:280px"></div>
  <div class="ribbon" style="left:138px;top:155px;width:134px;height:37px;font-size:12px">
    <svg viewBox="0 0 134 37" preserveAspectRatio="none"><polygon points="0,0 134,0 124,18.5 134,37 0,37 10,18.5" fill="var(--ribbon)" stroke="var(--ink)" stroke-width="1.5"/></svg>
    <span>HOT BEVERAGE</span>
  </div>
  <ul class="price-list" style="left:53px;top:217px;width:282px">
    <li><span>Fruit Platter</span><span>$15</span></li>
    <li><span>Bacon Egg and Cheese Roll</span><span>$6.5</span></li>
    <li><span>Vegetarian Brekky Wrap</span><span>$6.5</span></li>
    <li><span>Ham and Cheese Croissant</span><span>$6</span></li>
    <li><span>Cheese and Tomato Croissant</span><span>$5.5</span></li>
    <li><span>Ham and Cheese French Toast</span><span>$6.5</span></li>
    <li><span>Assorted Yoghurts</span><span>$5.5</span></li>
    <li><span>Bircher Muesli</span><span>$5.5</span></li>
    <li><span>Chia Pudding</span><span>$5.5</span></li>
    <li><span>Granola and Yoghurt</span><span>$5.5</span></li>
    <li><span>Muffin</span><span>$4.5</span></li>
    <li><span>Mini Muffin</span><span>$2.5</span></li>
    <li><span>Juice</span><span>$8</span></li>
  </ul>

  <div class="panel" style="left:433px;top:175px;width:338px;height:280px"></div>
  <div class="ribbon" style="left:532px;top:155px;width:134px;height:37px;font-size:11.5px">
    <svg viewBox="0 0 134 37" preserveAspectRatio="none"><polygon points="0,0 134,0 124,18.5 134,37 0,37 10,18.5" fill="var(--ribbon)" stroke="var(--ink)" stroke-width="1.5"/></svg>
    <span>MORNING AND<br>AFTERNOON TEA</span>
  </div>
  <ul class="price-list" style="left:461px;top:217px;width:283px">
    <li><span>Fruit Platter</span><span>$15</span></li>
    <li><span>Muffin</span><span>$4.5</span></li>
    <li><span>Mini Muffin</span><span>$2.5</span></li>
    <li><span>Assorted Slices</span><span>$4</span></li>
    <li><span>Assorted Cookies from</span><span>$3</span></li>
    <li><span>Assorted Yoghurts</span><span>$5.5</span></li>
    <li><span>Chia Pudding</span><span>$5.5</span></li>
    <li><span>Banana Bread</span><span>$4.5</span></li>
    <li><span>Juice</span><span>$8</span></li>
  </ul>
  <div class="notes" style="left:461px;top:388px">
    <p>*Cups/Plates/Serviettes can be provided at a charge of $1 per person</p>
    <p>*Barista made coffee available</p>
  </div>

  <p class="contact" style="left:0;width:800px;top:463px;text-align:center;font-size:13px">Visit us instore to discuss catering options or call 0438 672 914 or email martha@velbrisco.com.au</p>
</section>

<section class="sheet sheet--back">
  <div class="brand brand--small">WARD<br>ROUNDS</div>
  <h1 class="menu-title">CATERING MENU</h1>

  <div class="panel" style="left:32px;top:138px;width:338px;height:424px"></div>
  <div class="ribbon" style="left:135px;top:116px;width:137px;height:40px;font-size:18px">
    <svg viewBox="0 0 137 40" preserveAspectRatio="none"><polygon points="0,0 137,0 127,20 137,40 0,40 10,20" fill="var(--ribbon)" stroke="var(--ink)" stroke-width="1.5"/></svg>
    <span>LUNCH</span>
  </div>
  <div class="lunch">
    <p><b>Sandwiches&nbsp; or Wraps $7.50</b> <i>Sandwiches cut into quarters – Wraps cut into thirds</i></p>
    <p><b>Ham:</b> <i>butter, pickle spread, cheese, tomato, champagne leg ham</i></p>
    <p><b>Turkey:</b> <i>butter, cranberry sauce, lettuce mix, tomato, turkey breast</i></p>
    <p><b>Sweet Chilli Chicken:</b> <i>butter, sweet chilli sauce, aioli, lettuce mix, tomato, cheese, sweet chilli chicken tenders</i></p>
    <p><b>Chicken Schnitzel:</b> <i>butter, aioli, lettuce mix, tomato, tasty cheese, chicken schnitzel</i></p>
    <p><b>Chicken and Avocado:</b> <i>butter, aioli, lettuce mix, tomato, cheese, chicken breast, avocado</i></p>
    <p><b>Egg:</b> <i>butter, lettuce mix, egg, aioli, parsley, spring onion</i></p>
    <p><b>Tuna:</b> <i>butter, lettuce, tuna, aioli, sundried tomato, spring onion</i></p>
    <p><b>B.L.T.:</b> <i>butter, aioli, lettuce, tomato, bacon</i></p>
    <p><b>Salad:</b> <i>butter, lettuce mix, red onion, cucumber, capsicum, tomato, avocado, tasty cheese</i></p>
    <p><b>Tandoori Chicken:</b> <i>butter, tzatziki, lettuce mix, tomato, tandoori chicken</i></p>
    <p><b>Waldorf Chicken:</b> <i>butter, cos lettuce, chicken, seeded mustard, celery, walnuts, aioli</i></p>
    <p><b>Chicken Ceasar:</b> <i>butter, aioli, cos lettuce, chicken, parmesan cheese, bacon</i></p>
    <p><b>Cajun Chicken:</b> <i>butter, lettuce mix, tomato, red onion, Cajun chicken</i></p>
    <p><b>-Barbeque Chicken: butter, BBQ,</b></p>
    <p><b>-Felafel:</b></p>
    <div class="gap"></div>
    <p><b>Foccacias $8.50</b></p>
    <p><i>Cut in half – please let us know if you want them toasted</i></p>
    <p><i>**Same options as wraps and sandwiches – Plus:</i></p>
    <p><b>Roast Veggie:</b> <i>butter, pesto, grilled eggplant, grilled zucchini, roasted capsicum, feta cheese, baby spinach</i></p>
    <p><b>Salami:</b> <i>butter, pesto, baby spinach, mild salami, roasted capsicum, olives, feta cheese</i></p>
    <p><b>Chicken Schnitzel:</b> <i>Butter, Housemade coleslaw, chicken schnitzel</i></p>
    <div class="gap"></div>
    <p><b>Bagels $9.0</b></p>
    <p><b>Turkey:</b> <i>butter, cranberry sauce, baby spinach, tomato, camembert cheese</i></p>
    <p><b>Smoked Salmon:</b> <i>butter, cream cheese, baby spinach, tomato, smoked salmon</i></p>
  </div>

  <div class="panel" style="left:433px;top:185px;width:338px;height:285px"></div>
  <div class="ribbon" style="left:532px;top:165px;width:136px;height:38px;font-size:17px">
    <svg viewBox="0 0 136 38" preserveAspectRatio="none"><polygon points="0,0 136,0 126,19 136,38 0,38 10,19" fill="var(--ribbon)" stroke="var(--ink)" stroke-width="1.5"/></svg>
    <span>HOT FOOD</span>
  </div>
  <ul class="price-list" style="left:461px;top:218px;width:280px">
    <li><span>Assorted Pies</span><span>$5.0</span></li>
    <li><span>Large tray hot chips</span><span>$15</span></li>
    <li><span>Small tray hot chips</span><span>$9</span></li>
    <li><span>Mini samosa</span><span>$3</span></li>
    <li><span>Vegetarian spring rolls</span><span>$3</span></li>
    <li><span>Party pies</span><span>$3</span></li>
    <li><span>Mini sausage rolls</span><span>$3</span></li>
    <li><span>Mini quiche</span><span>$3</span></li>
    <li><span>Mini dim sim</span><span>$2</span></li>
    <li><span>Sweet chilli chicken tenders</span><span>$3</span></li>
    <li><span>Meatballs</span><span>$2</span></li>
    <li><span>Spinach and ricotta pastizi</span><span>$3</span></li>
    <li><span>Vegetarian Frittata</span><span>$4.5</span></li>
    <li><span>Meat Frittata</span><span>$4.5</span></li>
  </ul>

  <p class="contact" style="left:432px;top:483px;width:300px;font-size:10px;line-height:13px">Visit us instore to discuss catering options or call 0438 672 914 or email martha@velbrisco.com.au</p>
</section>

</body>
</html>
```